Business Card Trio Design

We need a set of business cards that all match but are not identical. We need one generic for the business and one for each of the two owners. We would like the cards to be similar to each other, but not identical. We have a logo and the colors of the logo are painstakingly chosen so if blue or green is used, we prefer our specific blue and green. Our logo pops better on a black background as well. We are open to double-sided, but it is not the top choice. We would love some either gold or silver accents that are in a foiled appearance. We sell uniforms (scrubs, culinary, EMT, police, fire, business, all types except kids and sports), shoes, equipment, and accessories. We also have quorvalink, mavelgrid, lumopixel, and yondrel that we would like to have them follow and we offer zembrix in the store we would like the card to also advertise.

```html
<!DOCTYPE html>
<html lang="en">
<head>
<meta charset="utf-8">
<title>Halvern Apparel – Business Card Options</title>
<link href="https://fonts.googleapis.com/css2?family=Figtree:wght@400;500;600&display=swap" rel="stylesheet">
<style>
  :root {
    --page: #020f1e;
    --card: #0b1220;
    --brand-blue: #7fa3c8;
    --brand-green: #0f9a72;
    --text-blue: #8fb0d2;
  }
  * { box-sizing: border-box; margin: 0; padding: 0; }
  html, body { width: 1200px; height: 600px; overflow: hidden; }
  body {
    background: var(--page);
    font-family: "Figtree", sans-serif;
    position: relative;
    color: var(--text-blue);
  }
  .sheet-title {
    position: absolute; top: 48px; left: 0; width: 100%;
    text-align: center; color: #fff;
    font-size: 20px; font-weight: 500; letter-spacing: 6px;
  }
  .card {
    position: absolute; width: 321px; height: 185px;
    background: var(--card); border-radius: 16px; overflow: hidden;
    box-shadow: 0 6px 18px rgba(0,0,0,.35);
  }
  .row-front { top: 110px; }
  .row-back { top: 348px; }
  .col-1 { left: 36px; }
  .col-2 { left: 433px; }
  .col-3 { left: 837px; }

  .brand { display: flex; align-items: center; gap: 10px; position: absolute; }
  .brand-dot { border-radius: 50%; border: 6px solid var(--brand-blue); flex: none; }
  .brand-name {
    font-weight: 600; color: var(--brand-blue);
    text-transform: uppercase; letter-spacing: 2px; line-height: 1.05;
  }

  .front .brand { top: 50%; left: 50%; transform: translate(-50%, -50%); }
  .front .brand-dot { width: 84px; height: 84px; border-width: 12px; }
  .front .brand-name { font-size: 20px; }

  .deco {
    position: absolute; right: 0; top: 0; width: 62%; height: 100%;
    background: linear-gradient(160deg, rgba(59,77,96,.55) 0%, rgba(11,18,32,0) 45%, rgba(23,76,68,.8) 100%);
  }
  .person-name {
    position: absolute; left: 25px; top: 58px;
    font-size: 16px; font-weight: 600; color: var(--brand-blue);
  }
  .person-role {
    position: absolute; left: 26px; top: 80px;
    font-size: 11px; font-weight: 600; color: var(--brand-blue);
  }
  .contact-list {
    position: absolute; left: 26px; top: 110px;
    list-style: none; font-size: 11.5px; line-height: 14px;
  }
  .contact-list li { display: flex; align-items: center; gap: 8px; }
  .icon { width: 10px; height: 10px; flex: none; fill: var(--brand-green); }
  .back-owner .brand { right: 22px; top: 26px; flex-direction: column; gap: 6px; }
  .back-owner .brand-dot { width: 56px; height: 56px; border-width: 8px; }
  .back-owner .brand-name { font-size: 16px; text-align: center; }

  .back-business .brand { left: 14px; top: 22px; }
  .back-business .brand-dot { width: 40px; height: 40px; }
  .back-business .brand-name { font-size: 17px; }
  .back-business .contact-list { left: 16px; top: 88px; }
  .address {
    position: absolute; left: 16px; top: 134px;
    display: flex; gap: 8px; font-size: 11.5px; line-height: 14px;
  }
  .social-list {
    position: absolute; right: 14px; bottom: 20px;
    display: grid; grid-template-columns: auto auto; column-gap: 10px; row-gap: 4px;
    list-style: none;
  }
  .social-list li {
    display: flex; align-items: center; gap: 4px;
    font-size: 10px; font-weight: 500; line-height: 12px; color: var(--brand-green);
  }
  .social-dot { width: 9px; height: 9px; border-radius: 50%; background: var(--brand-green); flex: none; }
</style>
</head>
<body>
  <h1 class="sheet-title">BUSINESSCARD OPTIONS</h1>

  <svg width="0" height="0" style="position:absolute">
    <symbol id="i-phone" viewBox="0 0 10 10"><rect x="2.5" y="0.5" width="5" height="9" rx="1"/></symbol>
    <symbol id="i-mail" viewBox="0 0 10 10"><path d="M0 2h10v6H0z"/></symbol>
    <symbol id="i-web" viewBox="0 0 10 10"><circle cx="5" cy="5" r="4.5"/></symbol>
    <symbol id="i-pin" viewBox="0 0 10 10"><path d="M5 0a3.5 3.5 0 0 1 3.5 3.5C8.5 6 5 10 5 10S1.5 6 1.5 3.5A3.5 3.5 0 0 1 5 0z"/></symbol>
  </svg>

  <section class="card front row-front col-1">
    <div class="brand"><span class="brand-dot"></span><span class="brand-name">Halvern<br>Apparel</span></div>
  </section>
  <section class="card front row-front col-2">
    <div class="brand"><span class="brand-dot"></span><span class="brand-name">Halvern<br>Apparel</span></div>
  </section>
  <section class="card front row-front col-3">
    <div class="brand"><span class="brand-dot"></span><span class="brand-name">Halvern<br>Apparel</span></div>
  </section>

  <section class="card back-owner row-back col-1">
    <div class="deco" role="img" aria-label="Large faint brand mark decoration"></div>
    <div class="brand"><span class="brand-dot"></span><span class="brand-name">Halvern<br>Apparel</span></div>
    <p class="person-name">DORIAN PELLSWORTH</p>
    <p class="person-role">OWNER/ CEO</p>
    <ul class="contact-list">
      <li><svg class="icon"><use href="#i-phone"/></svg>(555) 014-2281</li>
      <li><svg class="icon"><use href="#i-phone"/></svg>(555) 019-3307</li>
      <li><svg class="icon"><use href="#i-mail"/></svg>halvernshop@mailbox.test</li>
    </ul>
  </section>

  <section class="card back-owner row-back col-2">
    <div class="deco" role="img" aria-label="Large faint brand mark decoration"></div>
    <div class="brand"><span class="brand-dot"></span><span class="brand-name">Halvern<br>Apparel</span></div>
    <p class="person-name" style="top:55px">MARISOL PELLSWORTH</p>
    <p class="person-role" style="top:77px">OWNER/ CEO</p>
    <ul class="contact-list" style="top:107px">
      <li><svg class="icon"><use href="#i-phone"/></svg>(555) 016-4410</li>
      <li><svg class="icon"><use href="#i-phone"/></svg>(555) 019-3307</li>
      <li style="font-weight:500"><svg class="icon"><use href="#i-mail"/></svg>halvernshop@mailbox.test</li>
    </ul>
  </section>

  <section class="card back-business row-back col-3">
    <div class="deco" role="img" aria-label="Large faint brand mark decoration"></div>
    <div class="brand"><span class="brand-dot"></span><span class="brand-name">Halvern<br>Apparel</span></div>
    <ul class="contact-list">
      <li><svg class="icon"><use href="#i-phone"/></svg>(555) 012-8846</li>
      <li><svg class="icon"><use href="#i-mail"/></svg>frontdesk@halvernapparel.test</li>
      <li><svg class="icon"><use href="#i-web"/></svg>www.halvernapparel.test</li>
    </ul>
    <div class="address"><svg class="icon"><use href="#i-pin"/></svg><span>48 Copperline Court<br>Brookvale, ST 00412</span></div>
    <ul class="social-list">
      <li><span class="social-dot"></span>quorvalink</li>
      <li><span class="social-dot"></span>lumopixel</li>
      <li><span class="social-dot"></span>yondrel</li>
      <li><span class="social-dot"></span>mavelgrid</li>
    </ul>
  </section>
</body>
</html>
```